Verpackungsdesign für Produkt gesucht
Zielgruppe
DE
Handelsunternehmen, weltweiter Vertrieb von unterschiedlichen Produkten unter eigenen Marken.
Neue internationale (Deutschland, EU) Marke in dem Segment Raucherprodukte.
Zielgruppe: Raucher
EN
Trading company, worldwide distribution of various products under own brands.
New international (Germany, EU) brand in the smoker products segment.
Target group: smokers
Aufgabenstellung
PRODUKT
- Markenname ist: brivt
- In diesem Fall benötigen wir ein Verpackungsdesign für das erste Produkt aus einer Reihe von
noch folgenden Produkten/Artikeln für Raucher.
Es besteht somit noch kein Markenbild oder andere Designs.
- Bei dem Produkt handelt es sich um einen durchsichtigen, ca. 2 cm langen Aufsteckfilter für
Zigaretten. Er wird auf eine Zigarette ohne Filter oder auf den eigentlichen Filter der Zigarette
gesteckt.
Der Filter ist durchsichtig konzipiert, damit man den gefilterten Schadstoffrückstand im Filter
sehen kann.
- Das Verpackungsdesign sollte clean und modern sein, für Mann und Frau.
- Verkauf über das Internet europaweit.
VERPACKUNG
Eine Idee für die Verpackungsform besteht bereits, jedoch sind auch offen für andere Vorschläge. Zur Orientierung bitte den Anhang ansehen! Dort haben wir Fotos hochgeladen, die ein Verpackungsmuster mit dem Produkt zeigen. Das Produkt im Bild hat einen gelben Filtereinsatz, unser Produkt wird jedoch einen orangefarbenen Filtereinsatz haben.
Bei der Verpackung handelt es sich um zwei Teile und beide sollen aus Karton sein:
1. Die Verpackung/Einzelpackung mit 50 Filtern Inhalt für das Produkt selbst
2. Eine Verpackung für fünf Einzelpackungen
Bei der Verpackung soll berücksichtigt werden, dass auf ihm ein Piktogramm mit Text auf der Vorderseite untergebracht werden muss, welches in verschiedenen Sprachen darauf hinweißt, dass Kunststoff nicht achtlos in die Umwelt entsorgt wird. Dieses Piktrogramm muss 6% der Fläche (Vorderseite auf der es gedruckt ist) einnehmen. Desweiteren muss ein Barcode angebracht werden. Beides ist ebenfalls im Anhang zu finden.
Was benötigen wir von Ihnen?
- Wir benötigen ein Design für beide Teile der Verpackung, natürlich soll auch der Markenname (brivt) auf der Verpackung ein schönes und modernes Design erhalten.

```html
<!DOCTYPE html>
<html lang="de">
<head>
<meta charset="utf-8">
<title>brivt – Schuber-Karton</title>
<link rel="stylesheet" href="https://fonts.googleapis.com/css2?family=Lato:wght@400&family=Roboto+Condensed:wght@400;700&display=swap">
<style>
  :root{
    --page:#f8f8f8;
    --ink:#1f4a66;
    --blue:#236287;
    --orange:#f7a21b;
    --orange-soft:#f9b94d;
    --white:#ffffff;
    --warn-red:#e03a4e;
    --warn-blue:#5ec8ee;
  }
  *{box-sizing:border-box;margin:0;padding:0}
  html,body{width:1200px;height:2164px;overflow:hidden;background:var(--page)}
  body{position:relative;font-family:"Roboto Condensed",sans-serif;color:var(--white)}
  .sheet-title{position:absolute;top:62px;left:0;width:1200px;text-align:center;
    font-family:"Lato",sans-serif;font-weight:400;font-size:42px;color:var(--ink);letter-spacing:1px}
  .panel{position:absolute;background:var(--blue)}
  .divider{border-right:1.5px solid var(--white)}

  /* Faltschachtel */
  .flap-top{left:192px;top:200px;width:356px;height:104px;border-bottom:1.5px solid var(--white)}
  .flap-top .flap-content{position:absolute;inset:0;transform:rotate(180deg)}
  .flap-top .count-block{position:absolute;left:22px;top:22px;line-height:1}
  .flap-top .count{font-weight:700;font-size:26px;color:var(--orange)}
  .flap-top .count small{font-weight:400;font-size:13px;margin-left:3px}
  .flap-top .desc{font-size:11px;margin-top:4px;line-height:1.35}
  .flap-top .code-field{position:absolute;left:149px;top:24px;width:59px;height:58px;
    background:var(--white);border-radius:9px}

  .side-left{left:87px;top:305px;width:105px;height:352px}
  .warning-badge{position:absolute;left:22px;top:30px;width:58px;height:116px;
    border:2px solid #111;display:flex}
  .warning-badge .badge-text{writing-mode:vertical-rl;background:var(--white);color:#111;
    font-size:8.5px;font-weight:700;width:12px;text-align:center;line-height:12px}
  .warning-badge .badge-art{flex:1;background:linear-gradient(var(--warn-red) 0 50%,var(--warn-blue) 50% 100%)}
  .warning-lines{position:absolute;left:20px;top:154px;height:190px;writing-mode:vertical-rl;
    font-size:8.5px;line-height:12px;letter-spacing:.2px}

  .front{left:192px;top:305px;width:356px;height:352px}
  .front .wordmark{position:absolute;left:-106px;top:132px;width:320px;text-align:center;
    transform:rotate(-90deg);font-size:86px;font-weight:700;letter-spacing:2px;line-height:1}
  .front .product-line{position:absolute;left:127px;top:18px;font-size:22px;letter-spacing:.5px}
  .front .cigarette-art{position:absolute;left:126px;top:50px;width:150px;height:70px;
    background:linear-gradient(180deg,rgba(255,255,255,0) 0%,rgba(255,255,255,.18) 55%,rgba(255,255,255,.55) 100%);
    border-radius:4px}
  .front .product-disc{position:absolute;left:134px;top:143px;width:184px;height:184px;border-radius:50%;
    background:var(--orange-soft);box-shadow:inset -8px -6px 0 var(--orange)}
  .front .product-art{position:absolute;left:52px;top:17px;width:66px;height:157px;
    background:linear-gradient(180deg,#eef3f7 0%,#e3ebf1 45%,#f2cf92 60%,#eef2f5 100%)}
  .front .count{position:absolute;left:128px;top:66px;font-weight:700;font-size:44px;color:var(--blue);line-height:1}
  .front .count small{display:block;font-weight:400;font-size:17px;margin-top:2px}

  .side-right{left:548px;top:305px;width:104px;height:352px}
  .side-right .web{position:absolute;left:34px;top:70px;writing-mode:vertical-rl;transform:rotate(180deg);
    font-size:22px;color:var(--orange);letter-spacing:1px}
  .side-right .web b{color:var(--white);font-size:28px}

  /* Schuber */
  .sleeve{left:755px;top:213px;width:351px;height:448px}
  .sleeve .window{position:absolute;left:3px;top:3px;right:3px;height:306px;border:1.5px solid var(--white)}
  .sleeve .label{position:absolute;left:0;right:0;top:317px;text-align:center;font-size:16px}
  .sleeve .rule{position:absolute;left:0;right:0;top:348px;border-top:2px solid var(--white)}
  .sleeve .brand{position:absolute;left:0;right:0;top:378px;text-align:center;font-weight:700;font-size:34px;color:var(--orange)}
</style>
</head>
<body>
  <h1 class="sheet-title">Schuber-Karton</h1>

  <section class="panel flap-top">
    <div class="flap-content">
      <div class="count-block">
        <div class="count">50<small>Stück</small></div>
        <div class="desc">Aufsteckfilter<br>für Zigaretten</div>
      </div>
      <div class="code-field"></div>
    </div>
  </section>

  <section class="panel side-left divider">
    <div class="warning-badge">
      <div class="badge-text">FILTER ENTHÄLT KUNSTSTOFF</div>
      <div class="badge-art" role="img" aria-label="Piktogramm: Kunststoff nicht in die Umwelt entsorgen"></div>
    </div>
    <div class="warning-lines">
      PLASTIC IN FILTER<br>FILTRE CONTENANT DU PLASTIQUE<br>PLASTICA NEL FILTRO<br>FILTER BEVAT PLASTIC<br>FILTRET INNEHÅLLER PLAST
    </div>
  </section>

  <section class="panel front divider">
    <div class="wordmark">brivt</div>
    <div class="product-line">Zigaretten-Aufsteckfilter</div>
    <div class="cigarette-art" role="img" aria-label="Illustration einer Zigarette mit Rauchfahne"></div>
    <div class="product-disc">
      <div class="product-art" role="img" aria-label="Illustration des durchsichtigen Aufsteckfilters mit orangefarbenem Einsatz"></div>
      <div class="count">50<small>Stück</small></div>
    </div>
  </section>

  <section class="panel side-right">
    <div class="web">www.<b>brivt</b>.de</div>
  </section>

  <section class="panel sleeve">
    <div class="window"></div>
    <div class="label">Zigaretten-Aufsteckfilter</div>
    <div class="rule"></div>
    <div class="brand">brivt</div>
  </section>
</body>
</html>
```